company, product, services, opportunity presentation

Lumivanta is a Payment Services Processor with value added product and services. We are focusing on the Payment Industry, Retail Merchants and Financial institutions. We have built total solution on QMO cloud to provide API based payment solutions such as Issuing of cards, Acquiring of payment transactions, Fraud prevention, Ecommerce, with customer facing APPs to provide dynamic virtual payment , 2FA and Passwordless sign in. Our focus is B2B .
We are developing our sales/investor pitch deck with slides covering company information, Market challengers (problems) that we are solving , Opportunities in the regional markets as well as global addressable Market for Payment cards. Lumivanta Product and services offerings to meet these challenges and opportunities.
Total Addressable Market statistics and data. Specific to virtual payment cards, Second factor authentication and digital ID (passwordless). Primarily data and justification for reducing Ecommerce card abandonment and increasing Authorization rates
Lumivanta Team and advisors’ slide. Current pipeline and customers. Use cases or case studies. Highlighting competitive advantage and USP. target clients and current pipline. Financials and projected spend in the next 2 years including target amount to raise fund. Solution and services slides and timeine of activities /roadmap
We need a PPT design to project better look and feel, crisp and eye catching graphic and design of the slides. clearer representation of key or salient points in all slides and information.

Target Market(s)

Financial Institutions, Retail (Merchants), Fintechs, Transportation

Industry/Entity Type

Cards and Payments Industry . Fraud prevention . Digital ID

Font styles to use
Sans Serif

Colors
F0912C
F2A743
F7CA91
FBE8D2
FDF5EE
EE7325
F08F49
F5BC92
FAE3D3
FDF4ED
A7469A
B969AE
D3A5CF
EDDBEB
F8F0F9
6B429C
8869AF
B7A5CE
E3DAEB
F3F0F8

Requirements
Must have
• problem to be solved, market challenges, market opportunities, product features and functionality. Use cases, Financial spend and funding. Team members and advisors. Timeline of roadmap for 2 years. competitive advantage and USP. Benefits to each customer segments
Nice to have
• Provision for future development on product and services. potentially covering other target markets such as Airlines, Insurance

```html
<!DOCTYPE html>
<html lang="en">
<head>
<meta charset="utf-8">
<title>Lumivanta – Company Presentation</title>
<link href="https://fonts.googleapis.com/css2?family=Montserrat:wght@500;600;700;800&family=Open+Sans:wght@400;600&display=swap" rel="stylesheet">
<style>
  :root{
    --page:#ebebeb;
    --white:#ffffff;
    --ink:#3a3a3a;
    --muted:#555555;
    --purple-deep:#4a1f5e;
    --purple:#6b429c;
    --magenta:#a7469a;
    --magenta-soft:#b969ae;
    --orange:#ee7325;
    --orange-soft:#f0912c;
    --grey-band:#f1f1f3;
  }
  *{box-sizing:border-box;margin:0;padding:0}
  html,body{width:1200px;height:4072px;overflow:hidden;background:var(--page)}
  body{font-family:"Open Sans",Arial,sans-serif;color:var(--ink)}
  .slide{position:absolute;left:48px;width:1104px;height:621px;background:var(--white);overflow:hidden}
  .brand{font-family:"Montserrat",Arial,sans-serif;font-weight:800;letter-spacing:.2px}
  .photo{position:absolute}
  h2{font-family:"Montserrat",Arial,sans-serif;font-weight:800;text-transform:uppercase}
  p{line-height:1.55}

  /* Slide 1 – welcome */
  .s-welcome{top:48px}
  .s-welcome .photo{inset:0;background:linear-gradient(120deg,#3d1650 0%,#7a2c84 45%,#a7469a 75%,#6b2a7a 100%)}
  .s-welcome .brand{position:absolute;top:140px;width:100%;text-align:center;color:var(--white);font-size:26px}
  .s-welcome h2{position:absolute;top:206px;width:100%;text-align:center;color:var(--white);font-size:46px}
  .s-welcome .rule{position:absolute;top:272px;left:352px;width:400px;height:2px;background:var(--white)}
  .s-welcome .lead{position:absolute;top:300px;width:100%;text-align:center;color:var(--white);font-size:19px}

  /* Slide 2 – problem */
  .s-problem{top:718px}
  .s-problem .photo{left:0;top:0;width:446px;height:621px;background:linear-gradient(160deg,#9aa7b7 0%,#5a6877 45%,#2c3440 100%)}
  .s-problem .content{position:absolute;left:500px;top:40px;width:560px}
  .s-problem .brand{font-size:26px;color:var(--orange)}
  .s-problem h2{margin-top:14px;font-size:24px;color:var(--ink)}
  .underline{display:block;width:60px;height:4px;background:var(--orange);margin-top:10px}
  .s-problem p{margin-top:22px;font-size:15px;color:var(--muted)}
  .s-problem ul{margin-top:24px;list-style:none}
  .s-problem li{position:relative;padding-left:26px;margin-bottom:18px;font-size:15px;line-height:1.5;color:var(--muted)}
  .s-problem li::before{content:"";position:absolute;left:4px;top:8px;width:7px;height:7px;border-radius:50%;background:var(--purple)}

  /* Slide 3 – challenges */
  .s-challenges{top:1388px}
  .s-challenges .photo.band{left:0;top:0;width:1104px;height:330px;background:linear-gradient(110deg,#4a1f5e 0%,#8a3a8c 50%,#c07ab8 100%)}
  .s-challenges .brand{position:absolute;top:40px;width:100%;text-align:center;color:var(--white);font-size:26px}
  .s-challenges .title{position:absolute;top:118px;left:0;width:100%;display:flex;justify-content:center;align-items:center;gap:22px}
  .s-challenges .title span{display:block;width:110px;height:2px;background:var(--white)}
  .s-challenges h2{color:var(--white);font-size:24px}
  .columns{position:absolute;left:40px;top:235px;width:1024px;display:flex;gap:42px}
  .column{width:313px}
  .column .thumb{height:118px}
  .column .bar{height:7px;background:var(--orange)}
  .column h3{margin-top:20px;font-family:"Montserrat",Arial,sans-serif;font-weight:800;font-size:17px;color:var(--purple)}
  .column p{margin-top:10px;font-size:14px;color:var(--muted)}

  /* Slide 4 – about */
  .s-about{top:2058px}
  .s-about .photo{left:0;top:0;width:610px;height:621px;background:linear-gradient(135deg,#3a1450 0%,#7e2f80 50%,#b65aa3 100%)}
  .s-about .edge{position:absolute;left:610px;top:0;width:8px;height:621px;background:var(--orange)}
  .s-about .content{position:absolute;left:660px;top:270px;width:400px}
  .s-about .heading{display:flex;align-items:baseline;gap:14px}
  .s-about h2{font-size:22px;color:var(--purple)}
  .s-about .brand{font-size:24px;color:var(--orange)}
  .s-about .rule{height:2px;background:var(--purple);margin-top:10px;width:400px}
  .s-about p{margin-top:26px;font-size:14px;color:var(--muted);text-align:justify}

  /* Slide 5 – opportunities */
  .s-opportunities{top:2728px}
  .s-opportunities h2{position:absolute;left:60px;top:40px;font-size:24px;color:var(--purple)}
  .s-opportunities .rule{position:absolute;left:0;top:84px;width:620px;height:2px;background:var(--purple)}
  .s-opportunities .brand{position:absolute;left:440px;top:104px;font-size:26px;color:var(--magenta)}
  .s-opportunities .photo.top{left:650px;top:20px;width:420px;height:290px;background:linear-gradient(150deg,#cfd8e4 0%,#8ea0b8 60%,#5d6f88 100%)}
  .s-opportunities .photo.bottom{left:580px;top:320px;width:490px;height:270px;background:linear-gradient(150deg,#b7c3cf 0%,#6f8194 60%,#3e4b5c 100%)}
  .s-opportunities .panel{position:absolute;left:0;top:160px;width:560px;height:430px;background:var(--purple-deep);padding:38px 40px 0 60px;color:var(--white)}
  .s-opportunities .panel p{font-size:13.5px;line-height:1.6;text-align:justify;color:#f1e6f3}
  .s-opportunities .panel p+p{margin-top:18px}

  /* Slide 6 – team */
  .s-team{top:3398px}
  .s-team .header{position:absolute;left:0;top:0;width:1104px;height:86px;background:var(--grey-band);display:flex;align-items:center;padding-left:40px}
  .s-team .brand{font-size:26px;color:var(--purple)}
  .s-team .divider{width:2px;height:34px;background:var(--orange);margin:0 22px}
  .s-team h2{font-size:22px;color:var(--purple)}
  .team{position:absolute;left:40px;top:120px;width:1024px;display:flex;gap:28px}
  .member{width:235px}
  .member .portrait{height:180px}
  .member h3{margin-top:16px;font-family:"Montserrat",Arial,sans-serif;font-weight:800;font-size:15px;color:var(--purple);text-transform:uppercase}
  .member .bar{width:40px;height:3px;background:var(--orange);margin-top:8px}
  .member p{margin-top:12px;font-size:12px;line-height:1.55;color:var(--muted)}
</style>
</head>
<body>

<section class="slide s-welcome">
  <div class="photo" role="img" aria-label="Hands using a laptop with a purple tint, full slide background"></div>
  <div class="brand">Lumivanta</div>
  <h2>Welcome to Lumivanta</h2>
  <div class="rule"></div>
  <p class="lead">Lumivanta is a Payment Services Processor with value added product and services.</p>
</section>

<section class="slide s-problem">
  <div class="photo" role="img" aria-label="Card being inserted into a payment terminal held in a hand"></div>
  <div class="content">
    <div class="brand">Lumivanta</div>
    <h2>Problem to be solved</h2>
    <span class="underline"></span>
    <p>There are many variations of passages of Lorem Ipsum available, but the majority have suffered alteration in some form, by injected humour, or randomised words which don't look even slightly believable. If you are going to use a passage of Lorem Ipsum, you need to be sure there isn't anything embarrassing hidden in the middle of text. All the Lorem Ipsum generators on the Internet tend to repeat predefined.</p>
    <ul>
      <li>Lorem Ipsum is simply dummy text of the printing and typesetting industry page when looking at its.</li>
      <li>There are many variations of passages of Lorem Ipsum available, but the majority have suffered alteration in some form.</li>
      <li>Contrary to popular belief, Lorem Ipsum is not simply random text. It has roots in a piece of classical Latin.</li>
      <li>It is a long established fact that a reader will be distracted by the readable content of a page when.</li>
    </ul>
  </div>
</section>

<section class="slide s-challenges">
  <div class="photo band" role="img" aria-label="Person typing on a laptop with a purple tint"></div>
  <div class="brand">Lumivanta</div>
  <div class="title"><span></span><h2>Market Challenges</h2><span></span></div>
  <div class="columns">
    <article class="column">
      <div class="thumb" role="img" aria-label="Shopper paying by card at a desk" style="background:linear-gradient(135deg,#d9c3a8,#8a6a52)"></div>
      <div class="bar"></div>
      <h3>LOREM IPSUM IS SIMPLY</h3>
      <p>There are many variations of passages of Lorem Ipsum available, but the majority have suffered alteration in some form, by injected humour, or randomised words which don't look even slightly believable. If you are going to use a passage of Lorem Ipsum, you need to be sure there isn't anything.</p>
    </article>
    <article class="column">
      <div class="thumb" role="img" aria-label="Card payment on a laptop keyboard" style="background:linear-gradient(135deg,#c9b59f,#5e4a3c)"></div>
      <div class="bar"></div>
      <h3>LOREM IPSUM IS SIMPLY</h3>
      <p>There are many variations of passages of Lorem Ipsum available, but the majority have suffered alteration in some form, by injected humour, or randomised words which don't look even slightly believable. If you are going to use a passage of Lorem Ipsum, you need to be sure there isn't anything.</p>
    </article>
    <article class="column">
      <div class="thumb" role="img" aria-label="Hands holding a bank card and phone" style="background:linear-gradient(135deg,#c4ccd6,#6a7482)"></div>
      <div class="bar"></div>
      <h3>LOREM IPSUM IS SIMPLY</h3>
      <p>There are many variations of passages of Lorem Ipsum available, but the majority have suffered alteration in some form, by injected humour, or randomised words which don't look even slightly believable. If you are going to use a passage of Lorem Ipsum, you need to be sure there isn't anything.</p>
    </article>
  </div>
</section>

<section class="slide s-about">
  <div class="photo" role="img" aria-label="Online shopping on a laptop with shopping cart icons, purple tint"></div>
  <div class="edge"></div>
  <div class="content">
    <div class="heading"><h2>About us</h2><span class="brand">Lumivanta</span></div>
    <div class="rule"></div>
    <p>Lumivanta is a Payment Services Processor with value added product and services. We are focusing on the Payment Industry, Retail Merchants and Financial Institutions. We have built total solution on QMO cloud to provide API based payment solutions, such as Issuing of cards, Acquiring of payment transactions, Fraud prevention, Ecommerce, with Customer facing APPs to provide dynamic virtual payment, 2FA and Passwordless Sign in. Our focus is B2B.</p>
  </div>
</section>

<section class="slide s-opportunities">
  <h2>Market Opportunities</h2>
  <div class="rule"></div>
  <div class="brand">Lumivanta</div>
  <div class="photo top" role="img" aria-label="Business charts and reports on a desk"></div>
  <div class="photo bottom" role="img" aria-label="Team reviewing figures on a tablet and laptop"></div>
  <div class="panel">
    <p>Sed ut perspiciatis unde omnis iste natus error sit voluptatem accusantium doloremque laudantium, totam rem aperiam, eaque ipsa quae ab illo inventore veritatis et quasi architecto beatae vitae dicta sunt explicabo. Nemo enim ipsam voluptatem quia voluptas sit aspernatur aut odit aut fugit, sed quia consequuntur magni dolores eos qui ratione voluptatem sequi nesciunt. Neque porro quisquam est, qui dolorem ipsum quia dolor sit amet, consectetur, adipisci velit, sed quia non numquam eius modi tempora incidunt ut labore et dolore magnam aliquam quaerat voluptatem.</p>
    <p>Ut enim ad minima veniam, quis nostrum exercitationem ullam corporis suscipit laboriosam, nisi ut aliquid ex ea commodi consequatur? Quis autem vel eum iure reprehenderit qui in ea voluptate velit esse quam nihil molestiae consequatur, vel illum qui dolorem eum fugiat quo voluptas nulla pariatur.</p>
  </div>
</section>

<section class="slide s-team">
  <header class="header">
    <span class="brand">Lumivanta</span>
    <span class="divider"></span>
    <h2>Team members and advisors</h2>
  </header>
  <div class="team">
    <article class="member">
      <div class="portrait" role="img" aria-label="Portrait photo of team member" style="background:linear-gradient(160deg,#d7d9dd,#8d939c)"></div>
      <h3>Corwin</h3><div class="bar"></div>
      <p>At vero eos et accusamus et iusto odio dignissimos ducimus qui blanditiis praesentium voluptatum deleniti atque corrupti quos dolores et quas molestias excepturi sint occaecati cupiditate non provident, similique sunt in culpa qui officia deserunt mollitia animi, id est laborum et dolorum fuga. Et harum quidem rerum facilis est et expedita distinctio. Nam libero tempore, cum soluta nobis est eligendi optio cumque nihil impedit quo minus.</p>
    </article>
    <article class="member">
      <div class="portrait" role="img" aria-label="Portrait photo of team member" style="background:linear-gradient(160deg,#5a5f68,#23262b)"></div>
      <h3>Anselm T. Vrabel</h3><div class="bar"></div>
      <p>At vero eos et accusamus et iusto odio dignissimos ducimus qui blanditiis praesentium voluptatum deleniti atque corrupti quos dolores et quas molestias excepturi sint occaecati cupiditate non provident, similique sunt in culpa qui officia deserunt mollitia animi, id est laborum et dolorum fuga. Et harum quidem rerum facilis est et expedita distinctio. Nam libero tempore, cum soluta nobis est eligendi optio cumque nihil impedit quo minus.</p>
    </article>
    <article class="member">
      <div class="portrait" role="img" aria-label="Portrait photo of advisor" style="background:linear-gradient(160deg,#c9d3de,#6f7f92)"></div>
      <h3>Quillan</h3><div class="bar"></div>
      <p>At vero eos et accusamus et iusto odio dignissimos ducimus qui blanditiis praesentium voluptatum deleniti atque corrupti quos dolores et quas molestias excepturi sint occaecati cupiditate non provident, similique sunt in culpa qui officia deserunt mollitia animi, id est laborum et dolorum fuga. Et harum quidem rerum facilis est et expedita distinctio. Nam libero tempore, cum soluta nobis est eligendi optio cumque nihil impedit quo minus.</p>
    </article>
    <article class="member">
      <div class="portrait" role="img" aria-label="Portrait photo of advisor" style="background:linear-gradient(160deg,#b9cde0,#4f6d8c)"></div>
      <h3>Harrowby</h3><div class="bar"></div>
      <p>At vero eos et accusamus et iusto odio dignissimos ducimus qui blanditiis praesentium voluptatum deleniti atque corrupti quos dolores et quas molestias excepturi sint occaecati cupiditate non provident, similique sunt in culpa qui officia deserunt mollitia animi, id est laborum et dolorum fuga. Et harum quidem rerum facilis est et expedita distinctio. Nam libero tempore, cum soluta nobis est eligendi optio cumque nihil impedit quo minus.</p>
    </article>
  </div>
</section>

</body>
</html>
```